Business Card Design Project

We require business cards to be produced with the following design
http://files.pixelvault-demo.net/img/50329/84172/84172_2093548_50329_image.jpg
Rather than bright meadow, please use Vantelo as the comapny name.
Please also use the following contact details:
1.
Daniel Overbeck
Entrepreneur
07423158871
doverbeck@vantelo-demo.com
2.
Tom Ashworth
Founder
07539402217
tashworth@vantelo-demo.com
Please add:
Facebook favicion facebook.com/vantelo
Linked in favicon linkedin/danieloverbeck
Skype favicon thomasashworth
Linked in favicon linkedin/thomasashworth
Skype favicon thomasashworth
Google Plus favicon tomashworth@mailbox-demo.net
To the back

```html
<!DOCTYPE html>
<html lang="en">
<head>
<meta charset="utf-8">
<title>Vantelo Business Card</title>
<link href="https://fonts.googleapis.com/css2?family=Arimo:wght@700&family=Ubuntu:wght@400;500;700&display=swap" rel="stylesheet">
<style>
  :root {
    --page: #ecebe8;
    --card-dark: #1e1c1d;
    --card-light: #ffffff;
    --brand-red: #ee1c25;
    --ink: #2b2b2b;
    --ink-soft: #444444;
    --watermark: #ececee;
    --icon: #3a3a3a;
  }
  * { box-sizing: border-box; margin: 0; padding: 0; }
  html, body {
    width: 1200px; height: 900px; overflow: hidden;
    background: var(--page);
  }
  .sheet {
    width: 1200px; height: 900px;
    display: flex; flex-direction: column;
    align-items: center; justify-content: center; gap: 50px;
  }
  .card {
    position: relative;
    width: 630px; height: 360px;
    overflow: hidden;
    box-shadow: 0 2px 8px rgba(0,0,0,.12);
  }
  /* Front */
  .card--front {
    background: var(--card-dark);
    display: flex; align-items: center; justify-content: center; gap: 22px;
  }
  .brand-dot {
    width: 64px; height: 64px; border-radius: 50%;
    background: var(--brand-red);
  }
  .brand-name {
    font-family: "Ubuntu", sans-serif; font-weight: 700;
    font-size: 52px; letter-spacing: 1px;
    color: #ffffff;
  }
  /* Back */
  .card--back { background: var(--card-light); }
  .back-decor {
    position: absolute; right: -110px; bottom: -150px;
    width: 420px; height: 420px; border-radius: 50%;
    background: var(--watermark);
  }
  .holder {
    position: absolute; left: 48px; top: 46px;
  }
  .holder__name {
    font-family: "Arimo", sans-serif; font-weight: 700;
    font-size: 30px; color: var(--brand-red);
  }
  .holder__role {
    font-family: "Arimo", sans-serif; font-weight: 700;
    font-size: 13px; letter-spacing: 1px; color: var(--ink-soft);
    margin-top: 4px;
  }
  .contact-list {
    position: absolute; left: 48px; top: 150px;
    list-style: none;
    font-family: "Ubuntu", sans-serif; font-weight: 500;
    font-size: 19px; color: var(--ink); line-height: 24px;
  }
  .contact-list li { display: flex; align-items: center; gap: 8px; }
  .contact-list .gap { margin-top: 12px; }
  .contact-icon { width: 12px; height: 12px; flex: none; }
  .contact-icon--social {
    width: 12px; height: 12px; border-radius: 2px; background: var(--icon);
  }
</style>
</head>
<body>
<main class="sheet">
  <section class="card card--front" aria-label="Card front">
    <span class="brand-dot"></span>
    <span class="brand-name">VANTELO</span>
  </section>

  <section class="card card--back" aria-label="Card back">
    <div class="back-decor"></div>
    <div class="holder">
      <h1 class="holder__name">Tom Ashworth</h1>
      <p class="holder__role">FOUNDER</p>
    </div>
    <ul class="contact-list">
      <li>
        <svg class="contact-icon" viewBox="0 0 12 12"><circle cx="6" cy="6" r="6" fill="#3a3a3a"/><path d="M4 3.2l1 1.3-.6.7c.4.8 1 1.4 1.8 1.8l.7-.6 1.3 1-.6 1.1C5.4 8.4 3.6 6.6 3 4.4z" fill="#fff"/></svg>
        07539402217
      </li>
      <li>
        <svg class="contact-icon" viewBox="0 0 12 12"><circle cx="6" cy="6" r="6" fill="#3a3a3a"/><circle cx="6" cy="6" r="2" fill="none" stroke="#fff" stroke-width="1.2"/></svg>
        tashworth@vantelo-demo.com
      </li>
      <li class="gap"><span class="contact-icon contact-icon--social" aria-label="Social page"></span>/vantelo</li>
      <li><span class="contact-icon contact-icon--social" aria-label="Professional profile"></span>/thomasashworth</li>
      <li><span class="contact-icon contact-icon--social" aria-label="Call handle"></span>thomasashworth</li>
      <li><span class="contact-icon contact-icon--social" aria-label="Personal email"></span>tomashworth@mailbox-demo.net</li>
    </ul>
  </section>
</main>
</body>
</html>
```